Mind blowing and web Design Needed For Online Retailer that sells everything from electronics etc

We are a company that will be selling everything from books to electronics in the same mold as rivendor.com
We need a clean sleek design in the quince mold. I want the website to be uncluttered but dynamic and inviting.
Dont want it too busy, so that won't scare the buyers to the site.
Please go to mellowdeals.com to see the website in its present incarnation. I would like to keep the present colours if possible, but if there is a better colour combination that will convey our message then feel free to go with that.
If you willl notice, our current logo is a figure reclining in a chair while everything it wants comes to it.
Our slogan is "Lazy is good!"
We would also like to have banners on the site with someone smiling to themselves with a caption saying "I was lazy today and got 20% off my laptop"
Our main competitor is tobrelli.com so we need our site to make a bigger impact
Target Market(s)
Internet savvy young people 16-50
Industry/Entity Type
Electronics
Look and feel

```html
<!DOCTYPE html>
<html lang="en">
<head>
<meta charset="utf-8">
<title>mellowdeals – Lazy is good!</title>
<link rel="stylesheet" href="https://fonts.googleapis.com/css2?family=Open+Sans:wght@400;600;700&family=Noto+Serif:wght@400;700&family=Oswald:wght@500&display=swap">
<style>
:root{
  --ink:#2b2b2b;
  --navy:#1f2f47;
  --orange:#f07a12;
  --gold:#f7b41c;
  --red:#e8141b;
  --line:#d9d9d9;
  --topbar:#1e2530;
  --nav-dark:#2a2e35;
  --footer-deep:#2e3642;
  --link-blue:#2f7fc5;
  --ph:#c9ced6;
}
*{box-sizing:border-box;margin:0;padding:0}
html,body{width:788px;height:1200px;overflow:hidden}
body{position:relative;background:#fff;font-family:"Open Sans",Arial,sans-serif;color:var(--ink);font-size:9px}
.abs{position:absolute}
.ph{position:absolute;border-radius:3px}

.topbar{left:0;top:0;width:788px;height:15px;background:var(--topbar);color:#fff;font-size:7.5px;text-align:right;padding-right:92px;line-height:15px}
.topbar span{margin:0 4px}

.logo-mark{left:92px;top:22px;width:62px;height:48px;background:linear-gradient(#f0ecc8,#e6dd86)}
.logo-name{left:96px;top:70px;font-size:9px;color:var(--ink)}
.slogan{left:175px;top:42px;font-family:"Noto Serif",Georgia,serif;font-size:18px;color:var(--navy)}

.cart{left:537px;top:37px;width:159px;height:30px;border:1px solid #bbb}
.cart-title{left:549px;top:36px;font-size:8.5px;color:var(--ink);background:#fff;padding:0 3px}
.cart-title b{color:var(--orange)}
.cart-note{left:546px;top:51px;font-size:7.5px}
.cart-bag{left:662px;top:28px;width:22px;height:36px;background:linear-gradient(#4aa8ea,#1f7ccb)}

.nav{left:92px;top:86px;width:604px;height:23px;background:linear-gradient(#4a4f58,var(--nav-dark));display:flex;font-size:8px;color:#fff;overflow:hidden}
.nav span{flex:auto;text-align:center;padding:0 2px;line-height:23px;border-right:1px solid #555;white-space:nowrap}
.nav .active{background:linear-gradient(#ffd65a,var(--gold))}

.search{left:92px;top:121px;width:416px;height:23px;border:1px solid var(--gold);display:flex}
.search-field{flex:1;font-style:italic;color:#666;line-height:21px;padding-left:28px;font-size:8.5px;position:relative}
.search-field svg{position:absolute;left:7px;top:5px}
.search-cat{width:79px;border-left:1px solid #ccc;line-height:21px;padding-left:10px;font-size:8.5px}
.search-btn{width:54px;background:var(--gold);color:#fff;font-style:italic;font-size:12px;line-height:21px;text-align:center;font-family:"Noto Serif",Georgia,serif}
.divider-v{left:521px;top:117px;width:1px;height:32px;background:var(--line)}
.truck{left:530px;top:117px;width:52px;height:26px;background:linear-gradient(#e8ecf1,#b7c3d2)}
.ship-title{left:591px;top:116px;font-family:"Noto Serif",Georgia,serif;font-size:12px;color:var(--orange)}
.ship-note{left:591px;top:131px;font-size:7px;white-space:nowrap}
.rule{left:92px;width:604px;height:1px;background:var(--line)}
.rule.thick{height:3px;background:#e3e3e3}

.banner{left:92px;top:164px;width:604px;height:235px;background:radial-gradient(circle at 30% 40%,#ffc73a,#f7a610 70%,#f09a0b)}
.banner-head{left:116px;top:192px;font-family:"Oswald",Impact,sans-serif;font-size:29px;line-height:40px;color:#fff;z-index:2;white-space:nowrap}
.banner-head em{font-style:normal;color:var(--red)}
.banner-btn{left:119px;top:303px;width:79px;height:25px;background:#222;border:1px solid #555;border-radius:3px;color:#fff;font-size:13px;line-height:23px;text-align:center}
.banner-art{left:432px;top:200px;width:256px;height:165px;background:linear-gradient(135deg,#6d7785,#3b8ad6 55%,#2c3440)}
.dots{left:118px;top:366px;display:flex;gap:5px}
.dots i{width:7px;height:7px;border-radius:50%;background:#fff}
.dots i.on{background:var(--red)}

.promo-h{font-family:"Noto Serif",Georgia,serif;font-size:12px;top:416px}
.promo-text{font-size:8.5px;line-height:12px;top:456px}
.price{color:var(--red);font-size:9px}
.pill{height:9px;border-radius:5px;background:linear-gradient(#6cb5ea,var(--link-blue));color:#fff;font-size:5.5px;line-height:9px;text-align:center;width:40px}
.vline{width:1px;background:var(--line)}

.sec-h{font-family:"Noto Serif",Georgia,serif;font-size:11.5px;color:var(--orange);left:96px}
.view-all{left:652px;width:40px;height:9px;border-radius:5px;background:linear-gradient(#aaa,#666);color:#fff;font-size:5.5px;line-height:9px;text-align:center}
.card-text{width:150px;text-align:center;font-size:8.5px;line-height:11.5px}
.card-price{width:150px;text-align:center}

.footer{left:0;top:980px;width:788px;height:220px;background:radial-gradient(ellipse at 50% 40%,#4a5566,var(--footer-deep))}
.f-h{top:1001px;font-family:"Noto Serif",Georgia,serif;font-size:11px;color:var(--gold)}
.f-input{left:92px;width:110px;height:20px;border-radius:4px;background:#252c36;border:1px solid #5b6573;color:#9aa3ad;font-size:7.5px;line-height:18px;padding-left:8px}
.f-btn{left:94px;top:1090px;width:44px;height:18px;border-radius:3px;background:linear-gradient(#c9c9c9,#8a8a8a);color:#fff;font-size:8px;text-align:center;line-height:18px}
.f-links{color:#fff;font-size:7.5px;line-height:15.5px}
.pay{top:1031px;width:28px;height:18px;border-radius:3px;background:#f2f2f2}
.fb{left:536px;top:997px;width:160px;height:150px;background:#fff;border:1px solid #ccc}
.fb-avatar{width:24px;height:24px;background:var(--ph)}
.fb-name{font-size:6px;color:#333;width:28px;text-align:center}
.copy{left:92px;top:1177px;color:#fff;font-size:7.5px}
.soc{top:1173px;width:17px;height:17px;border-radius:50%;background:#fff}
</style>
</head>
<body>

<div class="abs topbar"><span>Sign In</span>|<span>My Account</span>|<span>Order Status</span>|<span>Wishlist</span>|<span>About US</span>|<span>Help</span></div>

<div class="ph logo-mark" role="img" aria-label="Logo illustration: figure reclining in a chair"></div>
<div class="abs logo-name">mellowdeals</div>
<div class="abs slogan">Lazy is good!</div>

<div class="abs cart"></div>
<div class="abs cart-title"><b>Shopping Bag</b> (o items)</div>
<div class="abs cart-note">Spend ₦25, <b>Get FREE SHIPPING</b></div>
<div class="ph cart-bag" role="img" aria-label="Shopping bag illustration"></div>

<nav class="abs nav">
  <span class="active">Mobile Phones</span><span>Laptop &amp; Desktop Computers</span><span>Tablet PCs</span><span>Printers</span><span>Cameras</span><span>Video Games</span><span>Televisions</span><span>DVD Players</span><span>AC</span><span>Fridges</span><span style="border:0">Inverters</span>
</nav>

<div class="abs search">
  <div class="search-field"><svg width="13" height="13" viewBox="0 0 13 13"><circle cx="7.5" cy="5.5" r="4" fill="none" stroke="#6a8fb5" stroke-width="1.5"/><line x1="4.5" y1="8.5" x2="1" y2="12" stroke="#6a8fb5" stroke-width="2"/></svg>Search Products...</div>
  <div class="search-cat">All Products &nbsp;⌄</div>
  <div class="search-btn">Search</div>
</div>
<div class="abs divider-v"></div>
<div class="ph truck" role="img" aria-label="Delivery truck illustration"></div>
<div class="abs ship-title">FREE SHIPPING</div>
<div class="abs ship-note">Free Shipping on selected items.</div>

<div class="abs rule thick" style="top:156px"></div>

<section>
  <div class="ph banner" style="border-radius:0"></div>
  <div class="ph banner-art" role="img" aria-label="Photo of a laptop, tablet and smartphone"></div>
  <div class="abs banner-head">I WAS LAZY TODAY AND<br>GOT <em>20% OFF</em> MY LAPTOP</div>
  <div class="abs banner-btn">Buy Now!</div>
  <div class="abs dots"><i class="on"></i><i></i><i></i><i></i><i></i></div>
</section>

<section>
  <div class="abs promo-h" style="left:98px">Deals of the Week</div>
  <div class="ph" style="left:99px;top:446px;width:72px;height:52px;background:linear-gradient(#bcbcbc,#555)" role="img" aria-label="Digital camera photo"></div>
  <div class="abs promo-text" style="left:185px">Corvano DX-880<br>Digital Camera</div>
  <div class="abs price" style="left:185px;top:489px">₦249.99</div>
  <div class="abs pill" style="left:185px;top:509px">Learn More</div>

  <div class="abs vline" style="left:292px;top:415px;height:115px"></div>
  <div class="abs promo-h" style="left:300px">Pay On Delivery</div>
  <div class="ph" style="left:302px;top:437px;width:62px;height:62px;background:linear-gradient(#e9e9e9,#b33c5e)" role="img" aria-label="Card payment terminal illustration"></div>
  <div class="abs promo-text" style="left:374px">We Accept Cash on Delivery<br>Pay easy at your doorstep</div>
  <div class="abs price" style="left:374px;top:489px">₦-99.99</div>
  <div class="abs pill" style="left:375px;top:509px">Learn More</div>

  <div class="abs vline" style="left:495px;top:415px;height:115px"></div>
  <div class="abs promo-h" style="left:505px">Special Offer</div>
  <div class="ph" style="left:505px;top:445px;width:44px;height:61px;background:linear-gradient(#1d2a4a,#7b8fb8)" role="img" aria-label="DVD cover"></div>
  <div class="abs promo-text" style="left:564px">Lorem Ipsum is simply dummy<br>text typesetting industry</div>
  <div class="abs price" style="left:564px;top:489px">₦-39.99</div>
  <div class="abs pill" style="left:566px;top:509px">Learn More</div>
</section>

<div class="abs rule" style="top:540px"></div>

<section>
  <div class="abs sec-h" style="top:558px">Laptops &amp; Tablets</div>
  <div class="abs view-all" style="top:562px">View All</div>
  <div class="ph" style="left:100px;top:592px;width:115px;height:88px;background:linear-gradient(#d8e6f2,#9aa4ae)" role="img" aria-label="Laptop photo"></div>
  <div class="ph" style="left:255px;top:595px;width:115px;height:72px;background:linear-gradient(#5fb3e3,#444)" role="img" aria-label="Laptop, tablet and phone photo"></div>
  <div class="ph" style="left:420px;top:592px;width:118px;height:80px;background:linear-gradient(#4d6d9c,#222)" role="img" aria-label="Tablets photo"></div>
  <div class="ph" style="left:582px;top:596px;width:82px;height:56px;background:linear-gradient(#cfcfcf,#333)" role="img" aria-label="Navigation device photo"></div>
  <div class="abs vline" style="left:235px;top:585px;height:145px"></div>
  <div class="abs vline" style="left:398px;top:585px;height:145px"></div>
  <div class="abs vline" style="left:558px;top:585px;height:145px"></div>
  <div class="abs card-text" style="left:81px;top:686px">Lorem Ipsum is simply<br>dummy text</div>
  <div class="abs card-text" style="left:238px;top:686px">Lorem Ipsum is simply<br>dummy text</div>
  <div class="abs card-text" style="left:406px;top:686px">Lorem Ipsum is simply<br>dummy text</div>
  <div class="abs card-text" style="left:556px;top:686px">Lorem Ipsum is simply<br>dummy text</div>
  <div class="abs card-price price" style="left:81px;top:715px">₦200.00</div>
  <div class="abs card-price price" style="left:238px;top:715px">₦200.00</div>
  <div class="abs card-price price" style="left:406px;top:715px">₦200.00</div>
  <div class="abs card-price price" style="left:556px;top:715px">₦200.00</div>
</section>

<div class="abs rule" style="top:743px"></div>

<section>
  <div class="abs sec-h" style="top:759px">Books &amp; Eletronics</div>
  <div class="abs view-all" style="top:766px">View All</div>
  <div class="ph" style="left:118px;top:792px;width:56px;height:88px;background:linear-gradient(#2a2d38,#111)" role="img" aria-label="Book cover"></div>
  <div class="ph" style="left:274px;top:794px;width:66px;height:86px;background:linear-gradient(#2a2d38,#111)" role="img" aria-label="Book cover"></div>
  <div class="ph" style="left:431px;top:806px;width:100px;height:68px;background:linear-gradient(#2b2b2b,#0c0c0c)" role="img" aria-label="Flat screen television photo"></div>
  <div class="ph" style="left:587px;top:798px;width:86px;height:72px;background:linear-gradient(#3a3a3a,#111)" role="img" aria-label="Digital SLR camera photo"></div>
  <div class="abs vline" style="left:235px;top:786px;height:146px"></div>
  <div class="abs vline" style="left:398px;top:786px;height:146px"></div>
  <div class="abs vline" style="left:558px;top:786px;height:146px"></div>
  <div class="abs card-text" style="left:81px;top:888px">Lorem Ipsum is simply<br>dummy text</div>
  <div class="abs card-text" style="left:238px;top:888px">Lorem Ipsum is simply<br>dummy text</div>
  <div class="abs card-text" style="left:406px;top:888px">Lorem Ipsum is simply<br>dummy text</div>
  <div class="abs card-text" style="left:556px;top:888px">Lorem Ipsum is simply<br>dummy text</div>
  <div class="abs card-price price" style="left:81px;top:917px">₦200.00</div>
  <div class="abs card-price price" style="left:238px;top:917px">₦200.00</div>
  <div class="abs card-price price" style="left:406px;top:917px">₦200.00</div>
  <div class="abs card-price price" style="left:556px;top:917px">₦200.00</div>
</section>

<div class="abs rule" style="top:944px"></div>

<footer>
  <div class="abs footer"></div>
  <div class="abs f-h" style="left:92px">Our Newsletter!</div>
  <div class="abs f-input" style="top:1032px">Enter your name...</div>
  <div class="abs f-input" style="top:1058px">Enter your email...</div>
  <div class="abs f-btn">Submit</div>

  <div class="abs f-h" style="left:238px">Quick Links</div>
  <div class="abs f-links" style="left:239px;top:1027px">&nbsp;Mobile Phones<br>Tablet PCs<br>Printers<br>Cameras<br>&nbsp;Video Games</div>
  <div class="abs f-links" style="left:332px;top:1027px">Televisions<br>DVD Players<br>AC<br>Fridges<br>Inverters</div>

  <div class="abs f-h" style="left:404px">Payment methods</div>
  <div class="abs pay" style="left:408px" role="img" aria-label="Card badge"></div>
  <div class="abs pay" style="left:442px" role="img" aria-label="Card badge"></div>
  <div class="abs pay" style="left:477px" role="img" aria-label="Wallet badge"></div>

  <div class="abs fb"></div>
  <div class="ph" style="left:543px;top:1004px;width:26px;height:24px;background:linear-gradient(#f0ecc8,#e6dd86)" role="img" aria-label="Logo illustration"></div>
  <div class="abs" style="left:578px;top:1005px;font-size:6.5px;color:#3b5998">mellowdeals <span style="color:#555">-on Friendbook</span></div>
  <div class="abs" style="left:574px;top:1019px;width:28px;height:12px;border:1px solid #9aa;border-radius:2px;font-size:6px;text-align:center;line-height:10px;background:#eef">Like</div>
  <div class="abs" style="left:651px;top:1016px;width:38px;height:15px;background:#69a74e;color:#fff;font-size:8px;text-align:center;line-height:15px;border-radius:2px">Sign Up</div>
  <div class="abs" style="left:542px;top:1041px;font-size:6px;color:#333">560 people like <span style="color:#3b5998">mellowdeals</span></div>
  <div class="abs" style="left:542px;top:1052px;display:flex;gap:10px">
    <div><div class="fb-avatar" role="img" aria-label="Member photo"></div><div class="fb-name">Dana</div></div>
    <div><div class="fb-avatar" role="img" aria-label="Member photo"></div><div class="fb-name">Olin</div></div>
    <div><div class="fb-avatar" role="img" aria-label="Member photo"></div><div class="fb-name">Greta</div></div>
    <div><div class="fb-avatar" role="img" aria-label="Member photo"></div><div class="fb-name">Ines</div></div>
  </div>
  <div class="abs" style="left:542px;top:1096px;display:flex;gap:10px">
    <div><div class="fb-avatar" role="img" aria-label="Member photo"></div><div class="fb-name">Nora</div></div>
    <div><div class="fb-avatar" role="img" aria-label="Member photo"></div><div class="fb-name">Cal</div></div>
    <div><div class="fb-avatar" role="img" aria-label="Member photo"></div><div class="fb-name">Tessa</div></div>
    <div><div class="fb-avatar" role="img" aria-label="Member photo"></div><div class="fb-name">Joel</div></div>
  </div>
  <div class="abs" style="left:540px;top:1133px;width:152px;height:1px;background:#ddd"></div>
  <div class="abs" style="left:542px;top:1136px;font-size:5.5px;color:#666"><span style="display:inline-block;width:6px;height:6px;background:#3b5998;vertical-align:middle"></span> Friendbook social plugin</div>

  <div class="abs" style="left:0;top:1166px;width:788px;height:1px;background:#4e5968"></div>
  <div class="abs copy">Copyright©2012 mellowdeals. All Rights Reserved.</div>
  <div class="abs soc" style="left:638px"></div>
  <div class="abs soc" style="left:658px"></div>
  <div class="abs soc" style="left:679px"></div>
</footer>

</body>
</html>
```